2 x storefront vinyl request

We are transitioning to a storefront office and need two vinyls for the windows.

First vinyl: Use the Aldwick Partners logo, website (www.aldwickpartnersestates.example) and leasing office number ((555) 318-4726)

Second vinyl: Maintenance Division & phone number (555) 318-4726

```html
<!DOCTYPE html>
<html lang="en">
<head>
<meta charset="utf-8">
<title>Aldwick Partners – Storefront Vinyls</title>
<link rel="stylesheet" href="https://fonts.googleapis.com/css2?family=Arimo:wght@400;700&family=Archivo+Black&display=swap">
<style>
  :root {
    --ink: #1e1a1b;
    --paper: #ffffff;
  }
  html, body {
    margin: 0;
    padding: 0;
    width: 1200px;
    height: 1200px;
    overflow: hidden;
    background: var(--paper);
  }
  .canvas {
    position: relative;
    width: 1200px;
    height: 1200px;
    font-family: "Arimo", Arial, sans-serif;
    color: var(--ink);
  }
  .brand {
    position: absolute;
    left: 0;
    right: 0;
    display: flex;
    justify-content: center;
    align-items: center;
    gap: 18px;
  }
  .brand-mark {
    width: 54px;
    height: 54px;
    background: var(--ink);
    flex: none;
  }
  .brand-name {
    font-weight: 700;
    font-size: 44px;
    line-height: 1.05;
    text-transform: uppercase;
    color: var(--ink);
  }
  .brand-name span { display: block; }
  .phone-band {
    position: absolute;
    background: var(--ink);
    color: var(--paper);
    font-weight: 700;
    font-size: 49px;
    display: flex;
    align-items: center;
    justify-content: center;
  }

  /* First vinyl: leasing office */
  .vinyl-leasing {
    position: absolute;
    left: 60px;
    top: 376px;
    width: 467px;
    height: 427px;
    box-sizing: border-box;
    border: 13px solid var(--ink);
    border-bottom: none;
    background: var(--paper);
  }
  .vinyl-leasing .brand { top: 100px; }
  .vinyl-leasing .website {
    position: absolute;
    left: 0;
    right: 0;
    top: 282px;
    margin: 0;
    text-align: center;
    font-weight: 700;
    font-size: 18px;
    letter-spacing: 0.4px;
  }
  .vinyl-leasing .phone-band {
    left: -13px;
    right: -13px;
    bottom: 0;
    height: 79px;
  }

  /* Second vinyl: maintenance */
  .vinyl-maintenance {
    position: absolute;
    left: 640px;
    top: 360px;
    width: 500px;
    height: 443px;
  }
  .vinyl-maintenance .arc-title {
    position: absolute;
    left: 0;
    top: 0;
  }
  .arc-title text {
    font-family: "Archivo Black", "Arial Black", sans-serif;
    font-size: 35px;
    fill: var(--ink);
    letter-spacing: 1px;
  }
  .vinyl-maintenance .brand { top: 166px; }
  .vinyl-maintenance .phone-band {
    left: 8px;
    width: 483px;
    bottom: 0;
    height: 76px;
  }
</style>
</head>
<body>
<main class="canvas">

  <section class="vinyl-leasing" aria-label="Leasing office window vinyl">
    <div class="brand">
      <span class="brand-mark"></span>
      <span class="brand-name"><span>Aldwick</span><span>Partners</span></span>
    </div>
    <p class="website">www.aldwickpartnersestates.example</p>
    <div class="phone-band">(555) 318-4726</div>
  </section>

  <section class="vinyl-maintenance" aria-label="Maintenance division window vinyl">
    <svg class="arc-title" width="500" height="200" viewBox="640 360 500 200">
      <defs>
        <path id="title-arc" d="M 668 548 A 263 263 0 0 1 1132 548"/>
      </defs>
      <text text-anchor="middle">
        <textPath href="#title-arc" startOffset="50%">MAINTENANCE DIVISION</textPath>
      </text>
    </svg>
    <div class="brand">
      <span class="brand-mark"></span>
      <span class="brand-name"><span>Aldwick</span><span>Partners</span></span>
    </div>
    <div class="phone-band">(555) 318-4726</div>
  </section>

</main>
</body>
</html>
```